Venture Capital Firm Needs Website Redesign

We need a bold revamp of our website (https://halvenmoor.vc/)
which at the moment looks washed out. We want a crisp, fresh and unique look. Feel free to keep as much or as little content in the site. The only thing we need to keep is a team section. The site should convey a clear distinction between our 3 product lines: Venture Capital, Private Credit, and Crypto. Two versions of our logo are attached and they should not change. For design inspirations, we like http://www.plumridgecap.com/ for a more simple site and for a more built out site we like http://tallowgate.com/

Updates
Industry/Entity Type
Investment
Coding
Coded - Design and coding required
Number of Pages Required
1 page
Font styles to use
Colors
Designer to choose colors to be used in the design.
Requirements
Must have
- - Clear distinction between our 3 product lines: Venture Capital, Private Credit
- - Team section

Nice to have
- Some really creative aspect like http://www.plumridgecap.com/ has with the distinction between first, second, and third kind

```html
<!DOCTYPE html>
<html lang="en">
<head>
<meta charset="utf-8">
<title>Halvenmoor — Venture, Private Credit, Crypto</title>
<link rel="stylesheet" href="https://fonts.googleapis.com/css2?family=Poppins:wght@200;300;400;500;600&display=swap">
<style>
:root{
  --green:#a4b51c;
  --green-dark:#8c9b12;
  --ink:#1d1d1d;
  --text:#555;
  --muted:#8a8a8a;
  --line:#e3e3e3;
  --panel:#ececec;
  --night:#0d1013;
  --night-2:#1b1f22;
  --footer:#262626;
  --footer-bar:#3a3a3a;
  --white:#fff;
  --blob:#f3f3e6;
  --social:#2a78c2;
}
*{margin:0;padding:0;box-sizing:border-box}
html,body{width:1200px;height:4500px;overflow:hidden}
body{font-family:"Poppins",sans-serif;color:var(--text);background:var(--white);position:relative}
.abs{position:absolute}
/* hero */
.hero{position:absolute;left:0;top:0;width:1200px;height:720px;
  background:radial-gradient(ellipse at 60% 45%,#2a3034 0%,#14181b 45%,var(--night) 100%)}
.brand{position:absolute;left:108px;top:14px;display:flex;align-items:center;gap:12px}
.brand-ring{width:60px;height:60px;border:2px solid var(--green);border-radius:50%}
.brand-name{font-size:20px;font-weight:300;color:var(--white);letter-spacing:1px}
.nav{position:absolute;right:108px;top:36px;display:flex;gap:44px;list-style:none}
.nav li{font-size:13px;font-weight:400;color:var(--white);letter-spacing:.5px}
.hero-title{position:absolute;left:0;top:236px;width:1200px;text-align:center;
  font-size:52px;line-height:78px;font-weight:200;color:#d6d6d6}
/* generic section text */
.section-title{position:absolute;left:0;width:1200px;text-align:center;font-size:40px;font-weight:400;color:var(--ink)}
.section-title .accent{color:var(--green)}
.section-copy{position:absolute;left:245px;width:710px;text-align:center;font-size:11.5px;line-height:21px;color:var(--muted)}
.btn-more{position:absolute;left:530px;top:938px;width:140px;height:36px;border:1.5px solid #bbb;border-radius:18px;
  font-size:11px;font-weight:500;color:var(--ink);text-align:center;line-height:33px;letter-spacing:1px}
/* nodes */
.node{position:absolute;width:124px;height:124px;margin:-62px 0 0 -62px;border-radius:50%;background:var(--white);
  box-shadow:0 4px 18px rgba(0,0,0,.14);display:flex;align-items:center;justify-content:center;gap:6px}
.node-name{font-size:15px;font-weight:500;color:var(--ink)}
.node-dot{width:10px;height:10px;border-radius:50%;background:var(--green)}
/* chart */
.chart{position:absolute;left:250px;top:2800px}
/* team */
.team{position:absolute;left:0;top:3300px;width:1200px;height:816px;overflow:hidden;
  background:radial-gradient(ellipse at 50% 30%,#2e3336 0%,#16191b 55%,#0b0d0e 100%)}
.team-title{position:absolute;left:0;top:104px;width:1200px;text-align:center;font-size:38px;font-weight:400;color:var(--white)}
.team-copy{position:absolute;left:280px;top:170px;width:640px;text-align:center;font-size:11.5px;line-height:20px;color:#cfcfcf}
.card{position:absolute;top:255px;width:272px;height:435px;background:var(--white);border-radius:6px;overflow:hidden;
  box-shadow:0 6px 20px rgba(0,0,0,.35);text-align:center}
.card-photo{width:100%;height:255px;background:linear-gradient(180deg,#bdbdbd 0%,#7b7b7b 60%,#4a4a4a 100%)}
.card-name{margin-top:14px;font-size:21px;font-weight:400;color:var(--green)}
.card-role{font-size:12px;color:var(--muted);margin-top:2px}
.card-text{margin:10px auto 0;width:210px;font-size:11px;line-height:17px;color:var(--muted)}
.card-social{display:flex;justify-content:center;gap:8px;margin-top:14px}
.card-social span{width:20px;height:20px;border-radius:50%;background:var(--social)}
.arrow{position:absolute;top:455px;font-size:40px;font-weight:200;color:#777}
/* footer */
.footer{position:absolute;left:0;top:4116px;width:1200px;height:384px;background:var(--footer);color:#d0d0d0}
.footer-brand{position:absolute;left:110px;top:42px;font-size:40px;font-weight:300;color:var(--white);letter-spacing:3px}
.footer-brand-rule{position:absolute;left:110px;top:98px;width:36px;height:2px;background:var(--green)}
.footer-about{position:absolute;left:110px;top:110px;width:280px;font-size:11px;line-height:18px}
.footer-social{position:absolute;left:110px;top:210px;display:flex;gap:10px}
.footer-social span{width:26px;height:26px;border-radius:50%;background:var(--social)}
.footer-social span:last-child{background:#e2861f}
.footer-links{position:absolute;left:448px;top:50px;list-style:none}
.footer-links li{font-size:10.5px;line-height:31px;color:#e0e0e0}
.footer-head{position:absolute;top:48px;font-size:13px;font-weight:500;color:var(--white)}
.footer-head-rule{position:absolute;top:72px;width:30px;height:2px;background:var(--green)}
.contact-row{position:absolute;left:610px;display:flex;gap:12px;font-size:11.5px;line-height:17px;color:#e0e0e0}
.contact-row svg{flex:none;margin-top:2px}
.newsletter-label{position:absolute;left:885px;top:90px;font-size:11.5px;color:#e0e0e0}
.newsletter-input{position:absolute;left:885px;top:118px;width:200px;height:34px;background:var(--white)}
.newsletter-btn{position:absolute;left:885px;top:165px;width:112px;height:32px;background:var(--green);
  color:var(--white);font-size:10px;font-weight:500;line-height:32px;text-align:center;letter-spacing:.5px}
.footer-bar{position:absolute;left:110px;top:323px;width:980px;height:38px;background:var(--footer-bar);
  text-align:center;font-size:10.5px;line-height:38px;color:#ccc}
</style>
</head>
<body>

<header class="hero">
  <div class="brand"><span class="brand-ring"></span><span class="brand-name">Halvenmoor</span></div>
  <ul class="nav">
    <li>VENTURE</li><li>PRIVATE CREDIT</li><li>CRYPTO</li><li>ABOUT US</li><li>TEAM</li><li>BLOG</li><li>CONTACT</li>
  </ul>
  <h1 class="hero-title">Halvenmoor Operates<br>At The Intersection Of Technology<br>And Novel Asset Classes.</h1>
</header>

<h2 class="section-title" style="top:772px">Welcome to <span class="accent">Halvenmoor</span></h2>
<p class="section-copy" style="top:840px">Lorem ipsum dolor sit amet, consectetuer adipiscing elit, sed diam nonummy nibh euismod tincidunt ut laoreet dolore magna aliquam erat volutpat. Ut wisi enim ad minim veniam, quis nostrud exerci tation ullamcorper suscipit lobortis nisl ut aliquip ex ea commodo consequat. Duis autem vel eum iriure.</p>
<div class="btn-more">MORE</div>

<svg class="abs" style="left:0;top:1040px" width="1200" height="130" viewBox="0 0 1200 130" aria-hidden="true">
  <polygon points="0,30 1200,30 1200,130 0,130" fill="#f6f6f6"/>
  <polygon points="0,25 1200,25 1200,40 0,100" fill="#ffffff"/>
  <polygon points="0,15 390,92 0,100" fill="var(--green)"/>
</svg>

<h2 class="section-title" style="top:1176px">Venture Capital</h2>
<p class="section-copy" style="top:1242px">We invest in early stage startups led by founders who are passionate and knowledgeable about the markets they serve. We have our own software developers and product managers. We work with the founders in our portfolio to help them bring products to market, earning equity for this work and for the cash we invest in their companies.</p>
<svg class="abs" style="left:400px;top:1350px" width="400" height="400" viewBox="0 0 400 400" aria-hidden="true">
  <circle cx="200" cy="201" r="150" fill="none" stroke="var(--line)" stroke-width="6"/>
  <circle cx="200" cy="201" r="132" fill="var(--panel)"/>
</svg>
<div class="node" style="left:600px;top:1404px"><span class="node-dot"></span><span class="node-name">Pixelkin</span></div>
<div class="node" style="left:435px;top:1554px"><span class="node-name" style="font-size:13px">Marlow Group</span></div>
<div class="node" style="left:765px;top:1554px"><span class="node-name">Loomline</span></div>
<div class="node" style="left:600px;top:1698px"><span class="node-name">Kidlane</span></div>

<h2 class="section-title" style="top:1896px">Private Credit</h2>
<p class="section-copy" style="top:1962px">We invest in early stage startups led by founders who are passionate and knowledgeable about the markets they serve. We have our own software developers and product managers. We work with the founders in our portfolio to help them bring products to market, earning equity for this work and for the cash we invest in their companies.</p>
<svg class="abs" style="left:360px;top:2140px" width="480" height="330" viewBox="0 0 480 330" aria-hidden="true">
  <polygon points="240,26 30,296 450,296" fill="var(--panel)" stroke="var(--line)" stroke-width="6" stroke-linejoin="round"/>
</svg>
<div class="node" style="left:600px;top:2166px"><span class="node-dot"></span><span class="node-name">Seedwell</span></div>
<div class="node" style="left:390px;top:2436px"><span class="node-name" style="font-size:13px">Norvale Finance</span></div>
<div class="node" style="left:810px;top:2436px"><span class="node-name" style="font-size:13px">Brightledger</span></div>

<h2 class="section-title" style="top:2606px">Crypto</h2>
<p class="section-copy" style="top:2672px">We invest in early stage startups led by founders who are passionate and knowledgeable about the markets they serve. We have our own software developers and product managers. We work with the founders in our portfolio to help them bring products to market, earning equity for this work and for the cash we invest in their companies.</p>
<svg class="chart" width="700" height="400" viewBox="0 0 700 400" role="img" aria-label="Line chart of cumulative growth, fund index versus benchmark coin">
  <path d="M40,90 C60,20 200,40 320,60 C420,75 470,10 560,30 C690,60 700,220 640,300 C580,380 300,380 150,360 C40,345 10,200 40,90 Z" fill="var(--blob)"/>
  <text x="300" y="28" font-family="Poppins,sans-serif" font-size="10" fill="#333">HMX Cumulative Growth</text>
  <circle cx="258" cy="50" r="6" fill="var(--green)"/>
  <text x="270" y="54" font-family="Poppins,sans-serif" font-size="9" fill="#555">HMX (1230.80%)</text>
  <circle cx="370" cy="50" r="6" fill="#111"/>
  <text x="382" y="54" font-family="Poppins,sans-serif" font-size="9" fill="#555">Benchmark (777.97%)</text>
  <g font-family="Poppins,sans-serif" font-size="8.5" fill="#666" text-anchor="end">
    <text x="160" y="73">3000</text><text x="160" y="118">2500</text><text x="160" y="163">2000</text>
    <text x="160" y="208">1500</text><text x="160" y="253">1000</text><text x="160" y="298">500</text>
  </g>
  <g stroke="#e6e6d8" stroke-width="1">
    <line x1="168" y1="70" x2="580" y2="70"/><line x1="168" y1="115" x2="580" y2="115"/>
    <line x1="168" y1="160" x2="580" y2="160"/><line x1="168" y1="205" x2="580" y2="205"/>
    <line x1="168" y1="250" x2="580" y2="250"/><line x1="168" y1="295" x2="580" y2="295"/>
  </g>
  <g font-family="Poppins,sans-serif" font-size="8.5" fill="#666" text-anchor="middle">
    <text x="170" y="330">Jan</text><text x="198" y="330">Feb</text><text x="226" y="330">Mar</text><text x="254" y="330">Apr</text>
    <text x="282" y="330">May</text><text x="310" y="330">Jun</text><text x="338" y="330">Jul</text><text x="366" y="330">Aug</text>
    <text x="394" y="330">Sep</text><text x="422" y="330">Oct</text><text x="450" y="330">Nov</text><text x="478" y="330">Dec</text>
    <text x="506" y="330">Jan</text><text x="534" y="330">Feb</text><text x="562" y="330">Mar</text>
  </g>
  <polyline points="170,318 184,318 198,317 212,316 226,314 240,313 254,310 268,306 282,300 296,296 310,290 324,282 338,285 352,274 366,268 380,260 394,262 408,250 422,236 436,228 450,210 464,180 478,160 492,120 506,95 520,145 534,168 548,200 562,230" fill="none" stroke="var(--green)" stroke-width="3"/>
  <polyline points="170,318 184,318 198,318 212,318 226,317 240,316 254,315 268,313 282,310 296,307 310,305 324,300 338,302 352,296 366,292 380,288 394,290 408,283 422,276 436,270 450,256 464,230 478,208 492,190 506,215 520,238 534,252 548,264 562,275" fill="none" stroke="#111" stroke-width="3"/>
  <g fill="var(--green)">
    <circle cx="170" cy="318" r="2.5"/><circle cx="184" cy="318" r="2.5"/><circle cx="198" cy="317" r="2.5"/><circle cx="212" cy="316" r="2.5"/>
  </g>
</svg>

<section class="team">
  <svg class="abs" style="left:0;top:0" width="1200" height="816" viewBox="0 0 1200 816" aria-hidden="true">
    <g stroke="rgba(255,255,255,.07)" stroke-width="1" fill="none">
      <polyline points="0,120 180,60 320,160 520,40 760,110 940,30 1200,140"/>
      <polyline points="60,300 250,220 430,330 700,240 900,320 1120,220"/>
    </g>
    <polygon points="1200,500 1200,720 760,816 1200,816" fill="var(--green)"/>
  </svg>
  <h2 class="team-title">Our Team &amp; Values</h2>
  <p class="team-copy">We're a small team of smart, funny hard-working specialists who are pushing to become the #1 company in self-reliance. High ambition, radical honesty and a result-oriented mindset are encouraged at Halvenmoor.</p>
  <span class="arrow" style="left:112px">‹</span>
  <span class="arrow" style="right:112px">›</span>
  <article class="card" style="left:164px">
    <div class="card-photo" role="img" aria-label="Black and white portrait of Idris Calloway"></div>
    <h3 class="card-name">IDRIS CALLOWAY</h3>
    <p class="card-role">Partner</p>
    <p class="card-text">Idris started in early stage deals and backed 30 funded businesses before leading our credit strategy.</p>
    <div class="card-social"><span></span><span></span></div>
  </article>
  <article class="card" style="left:464px">
    <div class="card-photo" role="img" aria-label="Black and white portrait of Ravi Tendral"></div>
    <h3 class="card-name">RAVI TENDRAL</h3>
    <p class="card-role">Partner</p>
    <p class="card-text">Ravi started in early stage deals and backed 30 funded businesses before leading our venture strategy.</p>
    <div class="card-social"><span></span><span></span></div>
  </article>
  <article class="card" style="left:764px">
    <div class="card-photo" role="img" aria-label="Black and white portrait of Marek Solvan"></div>
    <h3 class="card-name">Marek Solvan</h3>
    <p class="card-role">CEO Fenwickly</p>
    <p class="card-text">Marek started in early stage deals and backed 30 funded businesses before building his own platform.</p>
    <div class="card-social"><span></span><span></span></div>
  </article>
</section>

<footer class="footer">
  <div class="footer-brand">HALVENMOOR</div>
  <div class="footer-brand-rule"></div>
  <p class="footer-about">Ipsum dolor sit amet, consectetuer adipiscing elit, sed diam nonummy nibh euismod tincidunt ut laoreet dolore magna aliquam. Dolor sit amet, consectetuer adipiscing elit.</p>
  <div class="footer-social"><span></span><span></span><span></span><span></span></div>
  <ul class="footer-links">
    <li>HOME</li><li>WHY CHOOSE US</li><li>OUR SERVICES</li><li>INDUSTRIES</li><li>CONTACT US</li><li>LOGIN</li><li>BLOG</li>
  </ul>
  <div class="footer-head" style="left:610px">CONTACT INFO</div>
  <div class="footer-head-rule" style="left:610px"></div>
  <div class="contact-row" style="top:94px">
    <svg width="14" height="18" viewBox="0 0 14 18" aria-hidden="true"><path d="M7,0 C3,0 0,3 0,7 C0,12 7,18 7,18 C7,18 14,12 14,7 C14,3 11,0 7,0 Z" fill="var(--green)"/><circle cx="7" cy="7" r="2.6" fill="var(--footer)"/></svg>
    <span>Ipsum dolor sit amet, consectet<br>uer adipiscing elit, sed</span>
  </div>
  <div class="contact-row" style="top:144px">
    <svg width="16" height="12" viewBox="0 0 16 12" aria-hidden="true"><rect x="0.5" y="0.5" width="15" height="11" fill="none" stroke="var(--green)"/><polyline points="0.5,0.5 8,7 15.5,0.5" fill="none" stroke="var(--green)"/></svg>
    <span>info@halvenmoor.vc</span>
  </div>
  <div class="contact-row" style="top:180px;font-weight:500">
    <svg width="16" height="16" viewBox="0 0 16 16" aria-hidden="true"><circle cx="8" cy="8" r="7" fill="var(--green)"/><circle cx="8" cy="8" r="2.5" fill="var(--footer)"/></svg>
    <span>555-0148-220</span>
  </div>
  <div class="footer-head" style="left:885px">STAY IN TOUCH</div>
  <div class="footer-head-rule" style="left:885px"></div>
  <div class="newsletter-label">Subscribe Our Monthly Newsletter</div>
  <div class="newsletter-input"></div>
  <div class="newsletter-btn">SUBSCRIBE</div>
  <div class="footer-bar">© Copyrights 2018, HALVENMOOR | Privacy Policy</div>
</footer>

</body>
</html>
```